Biz card for my counselling/social work practice

Biz card design for my counselling practice, focus on well-being, I am a social worker who also teaches meditation and workshops but my main focus for the card is my counselling practice. My website reveals a gentle flowing quality which I would life reflected in my card. This business card will be designed to share with other practitioners who are looking for support with their clients to take their healing to another level or well-being.

Target Market(s)

professionals seeking mental health counselling/men/women/ those seeking to improve their well-being through insight based counselling to optimize their lives and process trauma or limiting patterns

Industry/Entity Type

Counsellor

Contact Information for Business Card

Info on the card: perhaps text is aligned left?
Marla Finch, MSW, RSW
Counsellor
250.555.0142
info@marlafinch.ca
www.marlafinch.ca

Please use a modern font doesn’t need to be the one chosen below. Thank you

Font styles to use
Serif

Colors
3176b5
33a6d7
33b8a4
6b449b
abd037
d2a4cc
e55fa2

Requirements
Must have
• My business card details on front
• Backside
• Accelerated Resolution Sessions
• Cognitive Behavioural Support
• Mindfulness-Based Counselling
Nice to have
• I would like the card to be basic, (white or creme without too much bold colour) and with perhaps a stripe or band of vertical colour in blue or green (or a merge of colour) perhaps embossed or in a negative space. (this is one idea, but do not want the card to be too feminine or interest only women as i see men too so this is only an idea, but not 100 percent on this.
• I do not have a logo. I would prefer to heart from my website not to be used in the design as i am considering modifying this and re-branding.
Should not have
• too bold colours or bright yellow/blacks. i Like tones that are greens, blues.

```html
<!DOCTYPE html>
<html lang="en">
<head>
<meta charset="utf-8">
<title>Marla Finch — Business Card</title>
<link rel="stylesheet" href="https://fonts.googleapis.com/css2?family=Roboto:wght@500&family=Work+Sans:wght@400;500&display=swap">
<style>
  :root {
    --backdrop: #1d1d1d;
    --paper: #efefef;
    --purple: #6b479b;
    --purple-line: #8a73b4;
    --lime: #a9cb35;
    --ink: #333333;
    --white: #ffffff;
    --emboss: #dcdcdc;
  }
  * { margin: 0; padding: 0; box-sizing: border-box; }
  html, body {
    width: 1200px;
    height: 897px;
    overflow: hidden;
    background: var(--backdrop);
  }
  .stage {
    position: relative;
    width: 1200px;
    height: 897px;
  }
  .card {
    position: absolute;
    left: 326px;
    width: 549px;
    height: 299px;
  }
  .card-front {
    top: 126px;
    background: var(--paper);
    font-family: "Work Sans", sans-serif;
    color: var(--ink);
  }
  .brand-mark {
    position: absolute;
    top: 40px;
    right: 28px;
    font-family: "Work Sans", sans-serif;
    font-weight: 500;
    font-size: 15px;
    letter-spacing: 1px;
    color: var(--emboss);
  }
  .holder-name {
    position: absolute;
    left: 28px;
    top: 190px;
    font-family: "Roboto", sans-serif;
    font-weight: 500;
    font-size: 21px;
    color: var(--purple);
    letter-spacing: -0.2px;
  }
  .holder-role {
    position: absolute;
    left: 28px;
    top: 215px;
    font-size: 13px;
    letter-spacing: 0.3px;
  }
  .divider {
    position: absolute;
    left: 28px;
    top: 247px;
    width: 494px;
    height: 1px;
    background: var(--purple-line);
  }
  .contact-row {
    position: absolute;
    left: 28px;
    top: 264px;
    width: 494px;
    font-size: 13px;
    letter-spacing: 0.6px;
    white-space: nowrap;
    text-align: justify;
    text-align-last: justify;
  }
  .contact-label { color: var(--purple); }
  .card-back {
    top: 473px;
    background: var(--purple);
    text-align: center;
    font-family: "Work Sans", sans-serif;
    color: var(--white);
  }
  .welcome-title {
    position: absolute;
    left: 0;
    right: 0;
    top: 71px;
    font-family: "Roboto", sans-serif;
    font-weight: 500;
    font-size: 31px;
    letter-spacing: 2px;
    color: var(--lime);
  }
  .welcome-subtitle {
    position: absolute;
    left: 0;
    right: 0;
    top: 108px;
    font-size: 16.5px;
    letter-spacing: 1px;
  }
  .service-list {
    position: absolute;
    left: 0;
    right: 0;
    top: 147px;
    list-style: none;
    font-size: 17.5px;
    letter-spacing: 1.5px;
    line-height: 29px;
  }
</style>
</head>
<body>
<main class="stage">
  <section class="card card-front" aria-label="Business card front">
    <div class="brand-mark">Marla Finch</div>
    <h1 class="holder-name">Marla Finch, MSW, RSW</h1>
    <p class="holder-role">Counsellor</p>
    <div class="divider"></div>
    <p class="contact-row"><span class="contact-label">P</span> : 250.555.0142 | <span class="contact-label">E</span> : info@marlafinch.ca | <span class="contact-label">W</span> : www.marlafinch.ca</p>
  </section>

  <section class="card card-back" aria-label="Business card back">
    <h2 class="welcome-title">A GENTLE SPACE</h2>
    <p class="welcome-subtitle">Counselling, Insight &amp; Well-being</p>
    <ul class="service-list">
      <li>Accelerated Resolution Sessions</li>
      <li>Cognitive Behavioural Support</li>
      <li>Mindfulness-Based Counselling</li>
    </ul>
  </section>
</main>
</body>
</html>
```